Flyer
Zielgruppe
Wir sind ein ambulanter Pflegedienst, Wir versorgen hilfebedürftige Menschen. Haben sie schon Erfahrung mit ambulanten Pflegediensten?
Aufgabenstellung
Er sollte kurz und knapp sein, nicht zu viel Text.

```html
<!DOCTYPE html>
<html lang="de">
<head>
<meta charset="utf-8">
<title>Ambulante Pflege Berger &amp; Hollmann – Flyer</title>
<link href="https://fonts.googleapis.com/css2?family=Fira+Sans:wght@400;600&family=Montserrat:wght@700&family=Bebas+Neue&display=swap" rel="stylesheet">
<style>
  :root {
    --ink: #0e3a5f;
    --navy: #0b3766;
    --steel: #5a7590;
    --heart: #dc2f45;
    --tick: #2f3338;
    --red: #d24a5a;
    --green: #86c832;
    --paper: #ffffff;
  }
  * { margin: 0; padding: 0; box-sizing: border-box; }
  html, body { width: 848px; height: 1200px; overflow: hidden; background: var(--paper); }
  .flyer { position: relative; width: 848px; height: 1200px; background: var(--paper); color: var(--ink); }

  .brand { position: absolute; left: 190px; top: 218px; display: flex; align-items: center; gap: 14px; }
  .brand-name { font-family: "Montserrat", sans-serif; font-weight: 700; font-size: 25px; color: var(--navy); letter-spacing: 0.5px; }
  .brand-dot { width: 40px; height: 40px; border-radius: 50%; background: var(--steel); }

  .corner-mark { position: absolute; width: 85px; height: 85px; border-radius: 6px;
    background: linear-gradient(135deg, var(--red) 0%, var(--red) 50%, var(--green) 100%); opacity: .85; }
  .corner-mark.top-right { left: 736px; top: 43px; }
  .corner-mark.bottom-left { left: 28px; top: 1074px; }
  .corner-mark.bottom-right { left: 736px; top: 1074px; }

  .benefits { position: absolute; left: 0; right: 0; top: 328px; text-align: center;
    font-family: "Fira Sans", sans-serif; font-size: 30px; line-height: 44px; color: var(--ink); }
  .benefits li { list-style: none; padding: 0 120px; }
  .icon { display: inline-block; vertical-align: -4px; margin-right: 8px; }

  .cta { position: absolute; left: 0; right: 0; top: 684px; text-align: center;
    font-family: "Fira Sans", sans-serif; font-weight: 600; font-size: 30px; line-height: 44px; color: var(--navy); }

  .contact { position: absolute; left: 0; right: 0; top: 786px; text-align: center;
    font-family: "Montserrat", sans-serif; font-weight: 700; font-size: 22px; letter-spacing: 3.2px;
    line-height: 23px; color: var(--navy); text-transform: uppercase; }
  .contact p { margin-bottom: 24px; }
  .contact .indent { display: inline-block; padding-left: 160px; }

  .slogan { position: absolute; left: 0; right: 0; top: 1082px; text-align: center;
    font-family: "Bebas Neue", sans-serif; font-size: 30px; line-height: 26px; letter-spacing: 2px; color: var(--navy); }
</style>
</head>
<body>
<main class="flyer">
  <div class="corner-mark top-right" role="img" aria-label="Rot-grünes Pflegekreuz mit Händen"></div>

  <header class="brand">
    <span class="brand-name">BERGER &amp; HOLLMANN</span>
    <span class="brand-dot"></span>
  </header>

  <ul class="benefits">
    <li><svg class="icon" width="32" height="28" viewBox="0 0 32 28"><path d="M16 27 C6 19 1 14 1 8 A7 7 0 0 1 16 5 A7 7 0 0 1 31 8 C31 14 26 19 16 27Z" fill="var(--heart)"/></svg>Mit Herz &amp; Kompetenz für Ihre Pflege</li>
    <li><svg class="icon" width="32" height="28" viewBox="0 0 32 28"><path d="M3 16 L11 25 L29 2" fill="none" stroke="var(--tick)" stroke-width="4" stroke-linecap="round" stroke-linejoin="round"/></svg>Individuelle Betreuung &amp; Unterstützung</li>
    <li><svg class="icon" width="32" height="28" viewBox="0 0 32 28"><path d="M3 16 L11 25 L29 2" fill="none" stroke="var(--tick)" stroke-width="4" stroke-linecap="round" stroke-linejoin="round"/></svg>Professionelle Pflege im eigenen Zuhause</li>
    <li><svg class="icon" width="32" height="28" viewBox="0 0 32 28"><path d="M3 16 L11 25 L29 2" fill="none" stroke="var(--tick)" stroke-width="4" stroke-linecap="round" stroke-linejoin="round"/></svg>Hilfe im Alltag – genau da, wo Sie uns brauchen</li>
  </ul>

  <p class="cta"><svg class="icon" width="30" height="30" viewBox="0 0 24 24"><path d="M6.6 10.8a15 15 0 0 0 6.6 6.6l2.2-2.2a1 1 0 0 1 1-.25 11.4 11.4 0 0 0 3.6.57 1 1 0 0 1 1 1V20a1 1 0 0 1-1 1A17 17 0 0 1 3 4a1 1 0 0 1 1-1h3.5a1 1 0 0 1 1 1c0 1.25.2 2.45.57 3.57a1 1 0 0 1-.25 1z" fill="var(--tick)"/></svg>Kontaktieren Sie uns für eine<br>unverbindliche Beratung!</p>

  <section class="contact">
    <p><svg class="icon" width="16" height="26" viewBox="0 0 16 26"><circle cx="8" cy="7" r="6" fill="var(--heart)"/><rect x="7" y="12" width="2" height="12" fill="#777"/></svg>Adresse: Lindenhofweg 12<br>84501 Altbachtal</p>
    <p><svg class="icon" width="26" height="26" viewBox="0 0 24 24"><path d="M6.6 10.8a15 15 0 0 0 6.6 6.6l2.2-2.2a1 1 0 0 1 1-.25 11.4 11.4 0 0 0 3.6.57 1 1 0 0 1 1 1V20a1 1 0 0 1-1 1A17 17 0 0 1 3 4a1 1 0 0 1 1-1h3.5a1 1 0 0 1 1 1c0 1.25.2 2.45.57 3.57a1 1 0 0 1-.25 1z" fill="var(--tick)"/></svg>Telefon: 0170/5512387 K.Berger<br><span class="indent">0152/448901276 M.Hollmann</span></p>
    <p><svg class="icon" width="28" height="20" viewBox="0 0 28 20"><rect x="1" y="1" width="26" height="18" rx="2" fill="#e8ecef" stroke="#9aa4ad"/><path d="M1 1 L14 11 L27 1" fill="none" stroke="#9aa4ad"/></svg>E-Mail: info@pflege-altbach.de</p>
  </section>

  <p class="slogan">Wir kümmern uns -<br>zuverlässig, herzlich und professionell.</p>

  <div class="corner-mark bottom-left" role="img" aria-label="Rot-grünes Pflegekreuz mit Händen"></div>
  <div class="corner-mark bottom-right" role="img" aria-label="Rot-grünes Pflegekreuz mit Händen"></div>
</main>
</body>
</html>
```